Marta Business Card

My wife is going to start her own business with renting holiday appartments to tourists. She needs a design for a new business card... and a new web site.
Look at Stayvolt "Erholung auf dem Lindenwäldchen"

Target Market(s)

Give business card to prospects at any situation

Contact Information for Business Card

not sure what this means

Font styles to use
Script

Colors
fec41a
fee18a

Requirements
Must have
• My wife's handwriting is difficult to read:
Entspannen - Loslassen - Auftanken
Marta & das Lindenwäldchen
Urlaub an einem besonderen Ort
Marta Brecke
Grauer Pfad 7
18471 Alt Feldow
post@marta-brecke.de
www.lindenwaeldchen.net
Nice to have
• Beige background
Font like handwriting

```html
<!DOCTYPE html>
<html lang="de">
<head>
<meta charset="utf-8">
<title>Marta Brecke – Visitenkarte</title>
<link rel="stylesheet" href="https://fonts.googleapis.com/css2?family=Parisienne&family=Quicksand:wght@500&display=swap">
<style>
  :root {
    --stage: #2b2b2b;
    --gold: #fec41a;
    --gold-light: #fee18a;
    --brown: #2e140d;
    --brown-mid: #3a1c14;
    --green: #1d7a3c;
  }
  * { box-sizing: border-box; margin: 0; padding: 0; }
  html, body { width: 1200px; height: 913px; overflow: hidden; }
  body {
    background: var(--stage);
    position: relative;
    font-family: "Quicksand", sans-serif;
  }
  .card {
    position: absolute;
    width: 560px;
    height: 320px;
    border-radius: 2px;
    box-shadow: 0 14px 30px rgba(0,0,0,.55);
    overflow: hidden;
  }
  .card--contact { left: 60px; top: 90px; background: var(--gold); }
  .card--slogan { left: 580px; top: 500px; background: var(--brown); }

  .card__field {
    position: absolute;
    left: 0; right: 0;
    top: 46px; bottom: 46px;
  }
  .card--contact .card__field { background: var(--brown); }
  .card--slogan .card__field { background: var(--gold); }

  .card__rule {
    position: absolute;
    left: 0; right: 0;
    height: 2px;
  }
  .card--contact .card__rule { background: var(--gold); }
  .card--slogan .card__rule { background: var(--brown); }
  .card__rule--top { top: 8px; }
  .card__rule--bottom { bottom: 8px; }

  .flourish {
    position: absolute;
    left: 50%;
    width: 120px;
    height: 22px;
    margin-left: -60px;
    border-radius: 11px;
  }
  .card--contact .flourish { background: var(--gold); }
  .card--slogan .flourish { background: var(--brown); }
  .flourish--top { top: -4px; }
  .flourish--bottom { bottom: -4px; }

  .contact-list {
    position: absolute;
    inset: 0;
    display: flex;
    flex-direction: column;
    justify-content: center;
    align-items: center;
    gap: 14px;
    list-style: none;
  }
  .contact-list__item {
    display: flex;
    align-items: center;
    gap: 8px;
    color: var(--gold);
    font-size: 19px;
    letter-spacing: .3px;
  }
  .contact-list__item svg { width: 14px; height: 14px; flex: none; }
  .contact-list__divider {
    width: 300px;
    height: 1px;
    background: var(--gold-light);
    opacity: .85;
  }

  .slogan {
    position: absolute;
    inset: 0;
    display: flex;
    flex-direction: column;
    justify-content: center;
    align-items: center;
    text-align: center;
    font-family: "Parisienne", cursive;
    color: var(--green);
    font-size: 32px;
    line-height: 1.25;
  }
</style>
</head>
<body>

  <section class="card card--contact" aria-label="Visitenkarte Rückseite">
    <span class="card__rule card__rule--top"></span>
    <span class="card__rule card__rule--bottom"></span>
    <div class="card__field">
      <span class="flourish flourish--top" role="img" aria-label="Goldenes Rankenornament"></span>
      <ul class="contact-list">
        <li class="contact-list__item">
          <svg viewBox="0 0 14 14" aria-hidden="true"><circle cx="7" cy="7" r="7" fill="#fec41a"/><rect x="3" y="4.5" width="8" height="5.5" fill="#2e140d"/><path d="M3 4.5 L7 7.5 L11 4.5" stroke="#fec41a" stroke-width="1" fill="none"/></svg>
          post@marta-brecke.de
        </li>
        <li class="contact-list__divider"></li>
        <li class="contact-list__item">
          <svg viewBox="0 0 14 14" aria-hidden="true"><circle cx="7" cy="7" r="6.5" fill="#fec41a"/><ellipse cx="7" cy="7" rx="3" ry="6.5" stroke="#2e140d" stroke-width=".8" fill="none"/><line x1=".5" y1="7" x2="13.5" y2="7" stroke="#2e140d" stroke-width=".8"/></svg>
          www.lindenwaeldchen.net
        </li>
        <li class="contact-list__divider"></li>
        <li class="contact-list__item">
          <svg viewBox="0 0 14 14" aria-hidden="true"><path d="M7 13.5 C4 9.5 2 7.5 2 5 A5 5 0 0 1 12 5 C12 7.5 10 9.5 7 13.5Z" fill="#fec41a"/><circle cx="7" cy="5" r="1.8" fill="#2e140d"/></svg>
          Marta Brecke, Grauer Pfad 7, 18471 Alt Feldow
        </li>
      </ul>
      <span class="flourish flourish--bottom" role="img" aria-label="Goldenes Rankenornament"></span>
    </div>
  </section>

  <section class="card card--slogan" aria-label="Visitenkarte Vorderseite">
    <span class="card__rule card__rule--top"></span>
    <span class="card__rule card__rule--bottom"></span>
    <div class="card__field">
      <span class="flourish flourish--top" role="img" aria-label="Braunes Rankenornament"></span>
      <div class="slogan">
        <p>Entspannen - Loslassen - Auftanken</p>
        <p>Marta &amp; das Lindenwäldchen</p>
        <p>Urlaub an einem besonderen Ort</p>
      </div>
      <span class="flourish flourish--bottom" role="img" aria-label="Braunes Rankenornament"></span>
    </div>
  </section>

</body>
</html>
```